Business Carss for Harborview Church

Need a progressive looking/modern business card design for my church

Target Market(s)

Families and young adults

Industry/Entity Type

Religious

Contact Information for Business Card

2846 Willow Creek Rd.
Frankfort Ky
502-555-0147

Rev. Curtis Holloway
Slogan: Honor God and Make Discies

Font styles to use
Serif
Sans Serif
Decorative
Script

Colors
0555a3
3176b5

Requirements
Should not have
• Should not have a template look
• A unique out of the box look

```html
<!DOCTYPE html>
<html lang="en">
<head>
<meta charset="utf-8">
<title>Harborview Church – Business Cards</title>
<link rel="stylesheet" href="https://fonts.googleapis.com/css2?family=Arimo:wght@400;700&family=Source+Sans+3:wght@400;700&display=swap">
<style>
  :root {
    --page-bg: #e8eaed;
    --card-deep: #1a559b;
    --card-bright: #3176b5;
    --ink: #ffffff;
  }
  * { margin: 0; padding: 0; box-sizing: border-box; }
  html, body {
    width: 1200px;
    height: 1200px;
    overflow: hidden;
    background: var(--page-bg);
  }
  .sheet {
    position: relative;
    width: 1200px;
    height: 1200px;
  }
  .card {
    position: absolute;
    left: 174px;
    width: 852px;
    height: 514px;
    color: var(--ink);
  }
  .card--deep { top: 38px; background: var(--card-deep); }
  .card--bright { top: 624px; background: var(--card-bright); }

  .card__name {
    position: absolute;
    left: 88px;
    top: 52px;
    font-family: "Arimo", Arial, sans-serif;
    font-weight: 700;
    font-size: 67px;
    line-height: 76px;
    letter-spacing: 0.2px;
  }
  .contact {
    position: absolute;
    left: 82px;
    display: flex;
    align-items: center;
    gap: 16px;
    font-family: "Source Sans 3", "Myriad Pro", sans-serif;
  }
  .contact--address { top: 248px; }
  .contact--phone { top: 353px; }
  .contact__icon {
    width: 42px;
    height: 42px;
    flex: none;
  }
  .contact__text {
    font-size: 19px;
    line-height: 26px;
    text-transform: uppercase;
  }
  .contact__text--phone {
    font-weight: 700;
    font-size: 22px;
    letter-spacing: 0.3px;
  }
  .card__slogan {
    position: absolute;
    right: 58px;
    top: 432px;
    font-family: "Arimo", Arial, sans-serif;
    font-size: 22px;
    line-height: 28px;
  }
</style>
</head>
<body>
<main class="sheet">

  <section class="card card--deep">
    <h1 class="card__name">Rev.<br>Curtis Holloway</h1>
    <div class="contact contact--address">
      <svg class="contact__icon" viewBox="0 0 42 42" aria-hidden="true">
        <rect x="2" y="2" width="38" height="38" rx="8" fill="none" stroke="#fff" stroke-width="2.5"/>
        <path d="M11 21 L21 12 L31 21 Z" fill="#fff"/>
        <rect x="14" y="20" width="14" height="10" fill="#fff"/>
        <rect x="17" y="23" width="3" height="3" fill="var(--card-deep)"/>
        <rect x="22" y="23" width="3" height="3" fill="var(--card-deep)"/>
      </svg>
      <p class="contact__text">2846 Willow Creek Rd.<br>Frankfort KY</p>
    </div>
    <div class="contact contact--phone">
      <svg class="contact__icon" viewBox="0 0 42 42" aria-hidden="true">
        <rect x="2" y="2" width="38" height="38" rx="8" fill="none" stroke="#fff" stroke-width="2.5"/>
        <path d="M14 11 L18 11 L20 16 L17.5 18 C18.5 21 21 23.5 24 24.5 L26 22 L31 24 L31 28 C31 29.5 30 30.5 28.5 30.5 C20 30 12 22 11.5 13.5 C11.5 12 12.5 11 14 11 Z" fill="none" stroke="#fff" stroke-width="2" stroke-linejoin="round"/>
      </svg>
      <p class="contact__text contact__text--phone">502-555-0147</p>
    </div>
    <p class="card__slogan">Honor God and Make Discies</p>
  </section>

  <section class="card card--bright">
    <h2 class="card__name">Rev.<br>Curtis Holloway</h2>
    <div class="contact contact--address">
      <svg class="contact__icon" viewBox="0 0 42 42" aria-hidden="true">
        <rect x="2" y="2" width="38" height="38" rx="8" fill="none" stroke="#fff" stroke-width="2.5"/>
        <path d="M11 21 L21 12 L31 21 Z" fill="#fff"/>
        <rect x="14" y="20" width="14" height="10" fill="#fff"/>
        <rect x="17" y="23" width="3" height="3" fill="var(--card-bright)"/>
        <rect x="22" y="23" width="3" height="3" fill="var(--card-bright)"/>
      </svg>
      <p class="contact__text">2846 Willow Creek Rd.<br>Frankfort KY</p>
    </div>
    <div class="contact contact--phone">
      <svg class="contact__icon" viewBox="0 0 42 42" aria-hidden="true">
        <rect x="2" y="2" width="38" height="38" rx="8" fill="none" stroke="#fff" stroke-width="2.5"/>
        <path d="M14 11 L18 11 L20 16 L17.5 18 C18.5 21 21 23.5 24 24.5 L26 22 L31 24 L31 28 C31 29.5 30 30.5 28.5 30.5 C20 30 12 22 11.5 13.5 C11.5 12 12.5 11 14 11 Z" fill="none" stroke="#fff" stroke-width="2" stroke-linejoin="round"/>
      </svg>
      <p class="contact__text contact__text--phone">502-555-0147</p>
    </div>
    <p class="card__slogan">Honor God and Make Discies</p>
  </section>

</main>
</body>
</html>
```